Blue Quill - tailored CVs templates

Wanting 6 -8 C.V templates that are professional and can be used to sent to a human resource manager. The market base is wide so generic is best to cover all areas however a couple of designer templates would be great. The main type of customers requiring CVs are business oriented however there is retail, construction, health and all the key arers of employment.

Target Market(s)

Anyone applying for a job to human resource department

Industry/Entity Type

Business

Colors

Designer to choose colors to be used in the design.

Requirements
Must have
• a good layout, easy to read format, must be able to write details on for cusomters eg work experince etc.
Nice to have
• looking for a range of 6 - 8 differnet templates, majority geneic and couple desiger templates

```html
<!DOCTYPE html>
<html lang="en">
<head>
<meta charset="utf-8">
<title>Blue Quill – CV and Cover Page Template</title>
<link rel="stylesheet" href="https://fonts.googleapis.com/css2?family=Raleway:wght@300;400;500;600;700&display=swap">
<style>
  :root{
    --backdrop-top:#b4b4b4;
    --backdrop-bottom:#d5d5d5;
    --paper:#ffffff;
    --brand-blue:#2a5cb3;
    --band-blue:#4b86d3;
    --photo-tone-a:#8a8a86;
    --photo-tone-b:#3c3d42;
    --ink:#1c1c1c;
    --ink-soft:#4a4a4a;
    --white:#ffffff;
  }
  *{margin:0;padding:0;box-sizing:border-box}
  html,body{width:1200px;height:712px;overflow:hidden}
  body{
    font-family:"Raleway",Arial,sans-serif;
    background:linear-gradient(to bottom,var(--backdrop-top) 0 318px,var(--backdrop-bottom) 318px 100%);
    position:relative;color:var(--ink);
  }
  .page{position:absolute;top:57px;width:476px;height:611px;background:var(--paper);
    box-shadow:0 4px 14px rgba(0,0,0,.28)}
  .page--resume{left:133px}
  .page--cover{left:637px;width:474px}
  .sidebar{position:absolute;left:0;top:0;width:160px;height:100%;background:var(--brand-blue);color:var(--white)}
  .portrait{position:absolute;left:0;top:0;width:160px;height:139px;
    background:radial-gradient(ellipse at 50% 40%,var(--photo-tone-a),var(--photo-tone-b))}
  .name{position:absolute;left:18px;top:154px;line-height:27px;font-size:29px;letter-spacing:.3px}
  .name b{font-weight:700;display:block}
  .name span{font-weight:300;display:block}
  .role{position:absolute;left:18px;top:208px;font-size:11.5px;font-weight:300}
  .band{position:absolute;left:0;width:160px;height:17px;background:var(--band-blue);
    font-size:9.5px;font-weight:600;letter-spacing:1.6px;padding:3px 0 0 18px;text-transform:uppercase}
  .band--about{top:238px;letter-spacing:.4px}
  .band--refs{top:238px}
  .band--info{top:390px}
  .about{position:absolute;left:18px;top:275px;width:130px;font-size:8px;line-height:9.2px}
  .about p+p{margin-top:9px}
  .refs{position:absolute;left:18px;top:270px;width:132px}
  .ref-name{font-size:8px;font-weight:600;margin-bottom:8px}
  .ref-text{font-size:8.2px;font-weight:700;line-height:9.2px;margin-bottom:12px}
  .contact{position:absolute;left:18px;top:433px;list-style:none}
  .contact li{display:flex;align-items:flex-start;font-size:8px;font-weight:600;line-height:10.4px;margin-bottom:6.5px}
  .contact li:nth-child(3){margin-top:-1px}
  .contact svg{width:14px;height:14px;margin:4px 12px 0 0;flex:none;fill:var(--white)}
  .main{position:absolute;left:160px;top:0;right:0;height:100%}
  .section-head{position:absolute;left:17px;display:flex;align-items:center;width:274px}
  .section-head svg{width:19px;height:19px;flex:none}
  .section-head h2{font-size:12px;font-weight:600;color:var(--brand-blue);margin:0 10px 0 11px;text-transform:uppercase}
  .section-head::after{content:"";flex:1;height:1.5px;background:var(--ink)}
  .entry{position:absolute;left:46px;width:262px;display:flex}
  .entry time{width:56px;font-size:7.6px;font-weight:700;padding-top:2px}
  .entry h3{font-size:9.8px;font-weight:600;line-height:11px}
  .entry h4{font-size:7.6px;font-weight:500;line-height:10px}
  .entry p{font-size:6.3px;line-height:8.8px;color:var(--ink-soft);width:188px}
  .skills{position:absolute;left:45px;top:526px;display:grid;grid-template-columns:133px 133px;font-size:7.4px;font-weight:600}
  .skill{display:flex;align-items:center;height:9.2px}
  .skill span{width:58px}
  .skill i{display:block;height:3.4px;background:var(--ink)}
  .letter{position:absolute;left:204px;top:46px;width:250px;font-size:6.4px;line-height:9px;color:var(--ink-soft);text-align:justify}
  .letter p{margin-bottom:11px}
  .signature{position:absolute;left:204px;top:480px;width:110px;height:34px;background:linear-gradient(90deg,#ececec,#f6f6f6)}
  .sign-off{position:absolute;left:204px;top:525px;font-size:8px;font-weight:600;line-height:10.4px;text-decoration:underline}
</style>
</head>
<body>

<section class="page page--resume">
  <aside class="sidebar">
    <div class="portrait" role="img" aria-label="Portrait photo of the candidate"></div>
    <h1 class="name"><b>HOT</b><span>SHOT</span></h1>
    <div class="role">Grafhic &amp; Web Designers</div>
    <div class="band band--about">About Me</div>
    <div class="about">
      <p>Lorem ipsum doilor sit amet, coetur adipiscing elitorem m ilor sit amet, consectetur adipiscinelit orem um doilor sit amet consectetur adipi-scing elit.</p>
      <p>Lorem ipsum doilor sit amet, coetur adipiscing elitorem m ilor sit amet, consectetur adipiscinelit orem um doilor sit amet consectetur</p>
    </div>
    <div class="band band--info">Information</div>
    <ul class="contact">
      <li><svg viewBox="0 0 16 16"><circle cx="8" cy="5" r="3.5"/><path d="M1 15c0-4 3-6 7-6s7 2 7 6z"/></svg><div>Name<br>Blue Quill</div></li>
      <li><svg viewBox="0 0 16 16"><path d="M8 1a5 5 0 0 0-5 5c0 4 5 9 5 9s5-5 5-9a5 5 0 0 0-5-5zm0 7a2 2 0 1 1 0-4 2 2 0 0 1 0 4z"/></svg><div>Address<br>78210 Maple Road<br>city&nbsp; Provinte<br>state country</div></li>
      <li><svg viewBox="0 0 16 16"><path d="M2 5c0-2 3-3 6-3s6 1 6 3v1h-3V5H5v1H2zM4 7h8l2 7H2z"/><circle cx="8" cy="10.5" r="1.6" fill="#2a5cb3"/></svg><div>Phone<br>014567890212</div></li>
      <li><svg viewBox="0 0 16 16"><path d="M1 3h14v10H1z"/><path d="M1 3l7 6 7-6" stroke="#2a5cb3" stroke-width="1.4" fill="none"/></svg><div>Email<br>hello@bluequill.cv</div></li>
      <li><svg viewBox="0 0 16 16"><path d="M3 2l10 5-4 1.5 3.5 4-1.8 1.5-3.5-4L5 13z"/></svg><div>Website<br>www.bluequill.cv</div></li>
    </ul>
  </aside>

  <main class="main">
    <div class="section-head" style="top:17px">
      <svg viewBox="0 0 20 20"><circle cx="10" cy="10" r="10" fill="#2a5cb3"/><path d="M7 5v10M7 5h6l-1.5 2.5L13 10H7" stroke="#fff" stroke-width="1.4" fill="#fff"/></svg>
      <h2>Experience</h2>
    </div>
    <article class="entry" style="top:55px"><time>2012 -2020</time><div><h3>Web Design &amp; Development</h3><h4>Nour In Position</h4><p>Lorem ipsum doilor sit amet, consectetur adipiscing elitorem m doilor sit amet, consectetur adipiscing elit orem ipsum doilor sit amet consectetur adipiscing elit.</p></div></article>
    <article class="entry" style="top:115px"><time>2012 -2020</time><div><h3>Graphic Designer &amp; Development</h3><h4>Nour In Position</h4><p>Lorem ipsum doilor sit amet, consectetur adipiscing elitoremum doilor sit amet, consectetur adipiscing elit orem ipsum doilor sit amet consectetur adipiscing elit.</p></div></article>
    <article class="entry" style="top:174px"><time>2012 -2020</time><div><h3>Video Templates &amp; Development</h3><h4>Nour In Position</h4><p>Lorem ipsum doilor sit amet, consectetur adipiscing elitoremum doilor sit amet, consectetur adipiscing elit orem ipsum doilor sit amet consectetur adipiscing elit.</p></div></article>
    <article class="entry" style="top:233px"><time>2012 -2020</time><div><h3>Photography &amp; Vidio Editing</h3><h4>Nour In Position</h4><p>Lorem ipsum doilor sit amet, consectetur adipiscing elitorem um doilor sit amet, consectetur adipiscing elit orem ipsum doilor sit amet consectetur adipiscing elit.</p></div></article>

    <div class="section-head" style="top:288px">
      <svg viewBox="0 0 20 20"><circle cx="10" cy="10" r="10" fill="#2a5cb3"/><path d="M5 7l2.5 2.5L10 5.5l2.5 4L15 7l-1 6.5H6z" fill="#fff"/><path d="M6 14.5h8" stroke="#fff" stroke-width="1.2"/></svg>
      <h2>Education</h2>
    </div>
    <article class="entry" style="top:326px"><time>2012 -2020</time><div><h3>Web Design &amp; Development</h3><h4>Nour In Position</h4><p>Lorem ipsum doilor sit amet, consectetur adipiscing elitoremum doilor sit amet, consectetur adipiscing elit orem ipsum doilor sit amet consectetur adipiscing elit.</p></div></article>
    <article class="entry" style="top:386px"><time>2012 -2020</time><div><h3>Graphic Designer &amp; Development</h3><h4>Nour In Position</h4><p>Lorem ipsum doilor sit amet, consectetur adipiscing elitoremum doilor sit amet, consectetur adipiscing elit orem ipsum doilor sit amet consectetur adipiscing elit.</p></div></article>
    <article class="entry" style="top:445px"><time>2012 -2020</time><div><h3>Graphic Designer &amp; Development</h3><h4>Nour In Position</h4><p>Lorem ipsum doilor sit amet, consectetur adipiscing elitoremum doilor sit amet, consectetur adipiscing elit orem ipsum</p></div></article>

    <div class="section-head" style="top:493px">
      <svg viewBox="0 0 20 20"><circle cx="10" cy="10" r="10" fill="#2a5cb3"/><path d="M5.5 10.2l3 3 6-6.5" stroke="#fff" stroke-width="2" fill="none"/></svg>
      <h2>My Skills</h2>
    </div>
    <div class="skills">
      <div class="skill"><span>Photo Edit</span><i style="width:56px"></i></div>
      <div class="skill"><span>Photo Edit</span><i style="width:56px"></i></div>
      <div class="skill"><span>Vector Art</span><i style="width:46px"></i></div>
      <div class="skill"><span>Vector Art</span><i style="width:46px"></i></div>
      <div class="skill"><span>Web Layout</span><i style="width:56px"></i></div>
      <div class="skill"><span>Web Layout</span><i style="width:56px"></i></div>
      <div class="skill"><span>Motion</span><i style="width:44px"></i></div>
      <div class="skill"><span>Motion</span><i style="width:44px"></i></div>
      <div class="skill"><span>Word Docs</span><i style="width:32px"></i></div>
      <div class="skill"><span>Word Docs</span><i style="width:32px"></i></div>
      <div class="skill"><span>Sheets</span><i style="width:50px"></i></div>
      <div class="skill"><span>Sheets</span><i style="width:50px"></i></div>
    </div>
  </main>
</section>

<section class="page page--cover">
  <aside class="sidebar">
    <div class="portrait" role="img" aria-label="Portrait photo of the candidate"></div>
    <h1 class="name"><b>HOT</b><span>SHOT</span></h1>
    <div class="role">Grafhic &amp; Web Designers</div>
    <div class="band band--refs">Refrences</div>
    <div class="refs">
      <div class="ref-name">CLARA WREN</div>
      <div class="ref-text">Lorem ipsum doilor sit amet, coetur adipiscing elitorem m ilor sit amet, consectetur adip</div>
      <div class="ref-name">CLARA WREN</div>
      <div class="ref-text">Lorem ipsum doilor sit amet, coetur adipiscing elitorem m ilor sit amet, consectetur.</div>
    </div>
    <div class="band band--info">Information</div>
    <ul class="contact">
      <li><svg viewBox="0 0 16 16"><circle cx="8" cy="5" r="3.5"/><path d="M1 15c0-4 3-6 7-6s7 2 7 6z"/></svg><div>Name<br>Blue Quill</div></li>
      <li><svg viewBox="0 0 16 16"><path d="M8 1a5 5 0 0 0-5 5c0 4 5 9 5 9s5-5 5-9a5 5 0 0 0-5-5zm0 7a2 2 0 1 1 0-4 2 2 0 0 1 0 4z"/></svg><div>Address<br>78210 Maple Road<br>city&nbsp; Provinte<br>state country</div></li>
      <li><svg viewBox="0 0 16 16"><path d="M2 5c0-2 3-3 6-3s6 1 6 3v1h-3V5H5v1H2zM4 7h8l2 7H2z"/><circle cx="8" cy="10.5" r="1.6" fill="#2a5cb3"/></svg><div>Phone<br>014567890212</div></li>
      <li><svg viewBox="0 0 16 16"><path d="M1 3h14v10H1z"/><path d="M1 3l7 6 7-6" stroke="#2a5cb3" stroke-width="1.4" fill="none"/></svg><div>Email<br>hello@bluequill.cv</div></li>
      <li><svg viewBox="0 0 16 16"><path d="M3 2l10 5-4 1.5 3.5 4-1.8 1.5-3.5-4L5 13z"/></svg><div>Website<br>www.bluequill.cv</div></li>
    </ul>
  </aside>

  <main class="main">
    <div class="section-head" style="top:17px;width:272px">
      <svg viewBox="0 0 20 20"><circle cx="10" cy="10" r="10" fill="#2a5cb3"/><path d="M7 5v10M7 5h6l-1.5 2.5L13 10H7" stroke="#fff" stroke-width="1.4" fill="#fff"/></svg>
      <h2>Cover Page</h2>
    </div>
  </main>
  <div class="letter">
    <p>Lorem ipsum doilor sit amet, consectetur adipiscing elitorem m doilor sit amet, consectetur adipiscing elit orem ipsum doilor sit amet consectetur adipiscing elit.Lorem ipsum doilor sit amet, consectetur adipiscing elitorem m doilor sit amet, consectetur adipiscing elit orem ipsum doilor sit amet consectetur adipiscing elit.Lorem ipsum doilor sit amet, consectetur adipiscing elitorem m doilor sit amet, consectetur adipiscing elit orem ipsum doilor sit amet consectetur adipiscing elit.Lorem ipsum doilor sit amet, consectetur adipiscing elitorem m doilor sit amet, consectetur adipiscing elit orem ipsum doilor sit amet consectetur adipiscing elit.Lorem ipsum doilor sit amet, consectetur adipiscing elitorem m doilor sit amet, consectetur adipiscing elit orem ipsum doilor sit amet consectetur adipiscing elit.Lorem ipsum doilor sit amet, consectetur adipiscing elitorem m doilor sit amet, consectetur adipiscing elit orem ipsum doilor sit amet consectetur adipiscing elit.</p>
    <p>Lorem ipsum doilor sit amet, consectetur adipiscing elitorem m doilor sit amet, consectetur adipiscing elit orem ipsum doilor sit amet consectetur adipiscing elit.Lorem ipsum doilor sit amet, consectetur adipiscing elitorem m doilor sit amet, consectetur adipiscing elit orem ipsum doilor sit amet consectetur adipiscing elit.Lorem ipsum doilor sit amet, consectetur adipiscing elitorem m doilor sit amet.</p>
    <p>Lorem ipsum doilor sit amet, consectetur adipiscing elitorem m doilor sit amet, consectetur adipiscing elit orem ipsum doilor sit amet consectetur adipiscing elit.Lorem ipsum doilor sit amet, consectetur adipiscing elitorem m doilor sit amet, consectetur adipiscing elit orem ipsum doilor sit amet consectetur adipiscing elit.Lorem ipsum doilor sit amet, consectetur adipiscing elitorem m doilor sit amet, consectetur adipiscing elit orem ipsum doilor sit amet consectetur adipiscing elit.Lorem ipsum doilor sit amet, consectetur adipiscing elitorem m doilor sit amet, consectetur adipiscing elit orem ipsum doilor sit amet consectetur adipiscing elit.Lorem ipsum doilor sit amet, consectetur adipiscing elitorem m doilor sit amet, consectetur adipiscing elit orem ipsum doilor sit amet.</p>
    <p>Lorem ipsum doilor sit amet, consectetur adipiscing elitorem m doilor sit amet, consectetur adipiscing elit orem ipsum doilor sit amet consectetur adipiscing elit.Lorem ipsum doilor sit amet, consectetur adipiscing elitorem m doilor sit amet, consectetur adipiscing elit orem ipsum doilor sit amet consectetur adipiscing elit.Lorem ipsum doilor sit amet, consectetur adipiscing elitorem m doilor sit amet, consectetur adipiscing elit orem ipsum doilor sit amet consectetur adipiscing elit.Lorem ipsum doilor sit amet, consectetur adipiscing elitorem m doilor sit amet, consectetur adipiscing elit orem ipsum doilor sit amet consectetur adipiscing elit.Lorem ipsum doilor sit amet, consectetur adipiscing elitorem m doilor sit amet, consectetur adipiscing elit orem ipsum doilor sit amet consectetur adipiscing elit.Lorem ipsum doilor sit amet, consectetur adipiscing elitorem m doilor sit amet, consectetur adipiscing elit orem ipsum doilor sit amet consectetur adipiscing elit.Lorem ipsum doilor sit amet, consectetur adipiscing elitorem m doilor sit amet, consectetur adipiscing elit orem ipsum doilor sit amet consectetur adipiscing elit.Lorem ipsum doilor sit amet, consectetur adipiscing elitorem m doilor sit amet, consectetur adipiscing elit orem ipsum doilor sit amet consectetur adipiscing elit.Lorem ipsum doilor sit amet, consectetur adipiscing elit.</p>
  </div>
  <div class="signature" role="img" aria-label="Handwritten signature"></div>
  <div class="sign-off">Name<br>Blue Quill</div>
</section>

</body>
</html>
```